Colourful Bold Design for Pet Insurance Website

PLEASE NOTE THAT THIS PROJECT HAS BEEN EXTENDED. Please read the PROJECT EXTENSION DOCUMENT BEFORE STARTING WORK ON ANY DESIGNS.

We are looking for a colourful bold new template design for our JOOMLA HOMEPAGE and a matching design for our new WORDPRESS BLOG.

The website will help pet owners work out which insurance policy best meets their needs. The aim of the website is to explain policy differences in a plain clear manner.

The website will need to have a professional colourful image. It needs to be BOLD, CLEAN AND SHARP rather than soft, pastel and cuddly.

COLOUR SCHEME
The website needs to have a bold colourful design on a white background.
On the inner pages we will have five different types of policies which will be colour coded. We would ideally therefore like to incorporate five distinct colours in the design. See attached document for example of colour schemes we like.

LOGO
We want to keep the existing logo. Please find the file attached. You may though change the logo colours.

CONTENT
One of the reasons for the new design is that we want to change the style of the homepage and include new content. Our current homepage can be found at www.furrow-cover-polls.co.uk.

Content Required
Slideshow
Article Intro.. About Pet Insurance
Policy Lookup Box (see existing site… you can change the design of this)
Six link options (see links on left of current page)
Latest Reviews (List of 6)
Ad (Same dimensions as currently on homepage)

News and Comment Section - To include Three or Four Articles, Title, Intro to article (probably 3 or 4 lines .. about 400px wide), Read more link
Social Media Section
FaceFeed Plugin with Feed
Latest Tweets Plugin
Pet Charities Latest Tweets
Footer
Larger footer with lots of links grouped in sections

It does not need to include the clipart pic of the pets which is on the current homepage.

Examples of Websites and Templates We Like
http://www.pawlane.com/ (like colours… fonts…layout)
http://sitetheme.brightkiln.com/?template=upbeat&path=/... (like the clarity, "white" space etc)
http://www.layoutforge.com/demo/51872.html (like white space, clear easy to read fonts… don’t like colour scheme, size of top picture)
http://www.layoutforge.com/website-templates/63915.html (like colour scheme, use of white space)

FEEDBACK
I will provide lots of feedback on all designs submitted so that together we can get the best result.

For clarification this is a DESIGN ONLY project. Our website developer will view the designs before we make our final choice as he wants to ensure he can develop "sharp, practical and most importantly light weight web interface" from the design.

Just updated this brief to clarify design issues, content issues and to give some more examples of site designs I like. 

Please note that although we wish to keep the logo you can change the colours to suit your design. 

Please note that we have now added details of pictures we would be happy to use on the website.  We would prefer it if you used one of these.   Otherwise please ensure your picture includes a nice dog and nice cat and no people!

I have been delighted with the quality of the designs submitted for this project.  So much so that I am going to extend the project to include some additional inner pages.   The amended brief will be posted on here on Friday 10 May.   The deadline will be extended and the budget will also be increased. 

Reason: Additional inner pages now required. Budget will be increased. Revised brief to be posted on here Friday 10 May.

Target Market(s)

Pet owners in the UK who are confused about pet insurance. It therefore needs to be a bold design which is plain, clean and easy to read. It should use bold colours rather than pastels and should not use "cuddly" images.

Industry/Entity Type

Insurance

Requirements
Must have
• Bold clear and distinct colours (preferably 5)
Content as per uploaded file (not just content from existing site)
Easy to read fonts
Should not have
• Pastel colours
Cuddly images

```html
<!DOCTYPE html>
<html lang="en">
<head>
<meta charset="utf-8">
<title>Furrow Cover Polls UK</title>
<link href="https://fonts.googleapis.com/css2?family=Ubuntu:wght@400;500;700&family=Arimo:wght@400;700&display=swap" rel="stylesheet">
<style>
:root{
  --dark:#2b2b2b;--dark2:#4a4a4a;--blue:#3f8fd6;--blue-lt:#5aa2e0;--cyan:#12b3e8;
  --fb:#3b5998;--sky:#5db6ee;--orange:#f5821f;--plum:#6d2f52;--grey:#e6e6e6;
  --text:#333;--muted:#555;--white:#fff;
}
*{box-sizing:border-box;margin:0;padding:0}
html,body{width:864px;height:1200px;overflow:hidden}
body{position:relative;font-family:"Arimo",Arial,sans-serif;color:var(--text);
  background:linear-gradient(#e9e9e9 0,#e9e9e9 996px,#8dbff0 996px,#4f93dc 1200px)}
.abs{position:absolute}
.header{left:0;top:0;width:864px;height:130px;background:linear-gradient(#1f1f1f,#474747 93px,#3a3a3a 130px)}
.brand{left:74px;top:28px;font-family:"Ubuntu",sans-serif;font-weight:500;font-size:20px;line-height:19px;color:#cfe4f8}
.brand .dot{display:inline-block;width:22px;height:22px;border:3px solid #cfe4f8;border-radius:50%;vertical-align:middle;margin-right:8px}
.social{right:80px;top:16px;font-size:9px;color:#bbb;display:flex;gap:8px}
.nav{left:74px;top:93px;width:716px;height:37px;display:flex;background:linear-gradient(#f2f2f2,#cfcfcf)}
.nav a{flex:auto;text-align:center;line-height:37px;font-size:10px;font-weight:700;color:#333;text-decoration:none;letter-spacing:.3px;border-left:1px solid #bdbdbd}
.nav a.active{background:var(--blue-lt);color:#fff;border:0;flex:0 0 100px}
.page{left:74px;top:130px;width:716px;height:926px;background:#fff}
.hero{left:80px;top:152px;width:450px;height:236px;background:linear-gradient(#fbfbfb,#e8e8e8);border:1px solid #ddd}
.hero h1{position:absolute;left:12px;top:14px;font-family:"Ubuntu",sans-serif;font-size:17px;font-weight:500;color:var(--blue)}
.hero .l2{position:absolute;left:12px;top:42px;font-family:"Ubuntu",sans-serif;font-weight:500;font-size:15.5px;color:#444}
.hero .l3{position:absolute;left:12px;top:69px;font-family:"Ubuntu",sans-serif;font-size:13.5px;color:#555}
.hero .l4{position:absolute;left:12px;top:92px;font-family:"Ubuntu",sans-serif;font-size:17px;color:#555}
.hero .pets{position:absolute;left:220px;top:52px;width:225px;height:178px;border-radius:6px;background:radial-gradient(ellipse at 50% 60%,#d8d2c8,#eeeae4 70%,transparent 72%)}
.btn-learn{position:absolute;left:6px;top:188px;width:128px;height:32px;border-radius:8px;background:linear-gradient(#7dc0f2,#3f8fd6);border:2px solid #bfe0fa;color:#fff;font-family:"Ubuntu",sans-serif;font-weight:500;font-size:16px;text-align:center;line-height:28px}
.policy{left:545px;top:149px;width:234px;height:146px;background:var(--cyan)}
.policy h2{position:absolute;left:14px;top:6px;font-family:"Ubuntu",sans-serif;font-weight:500;font-size:17px;color:#fff}
.policy .field{position:absolute;left:11px;width:212px;height:26px;background:#fff;border-radius:13px}
.policy .go{position:absolute;right:12px;top:113px;width:68px;height:26px;border-radius:6px;background:linear-gradient(#555,#111);border:1px solid #fff;color:#fff;font-size:9px;font-weight:700;text-align:center;line-height:24px}
.ad{left:550px;top:312px;width:224px;height:179px;background:linear-gradient(#dff0fa 0,#dff0fa 68%,#d6281f 68%,#c41e18)}
.welcome-icon{left:81px;top:402px;width:26px;height:26px;border:3px solid var(--blue);border-radius:50%}
.welcome h2{position:absolute;left:127px;top:412px;font-family:"Ubuntu",sans-serif;font-weight:500;font-size:14px;color:var(--blue);white-space:nowrap}
.welcome-pic{left:84px;top:450px;width:110px;height:110px;background:radial-gradient(ellipse,#d9d4cc,#f3f1ee 70%,#fff 72%)}
.welcome-txt{left:211px;top:438px;width:310px;font-size:8.6px;line-height:13px;color:#222}
.welcome-txt p{margin-bottom:13px}
.more{left:457px;top:569px;width:62px;height:17px;background:linear-gradient(#5aa2e0,#1f6fc2);border:1px solid #9ccaf0;border-radius:4px;color:#fff;font-size:8.5px;text-align:center;line-height:15px}
.rule{height:1px;background:#ddd}
.news-h{left:84px;top:612px;font-family:"Ubuntu",sans-serif;font-weight:500;font-size:14px;color:var(--blue)}
.news-item{left:84px;width:444px}
.news-item h3{font-size:8.8px;font-weight:700;padding-left:10px;position:relative}
.news-item h3::before{content:"";position:absolute;left:0;top:2px;border:3px solid transparent;border-left:3px solid var(--blue)}
.news-item p{margin:7px 0 0 10px;font-size:8.6px;line-height:11.5px;color:#444;width:430px}
.news-item .rm{text-align:right;font-size:8.6px;font-weight:700;color:#444;margin:2px 10px 3px 0}
.news-item .rule{margin-left:10px;background:#ccc}
.lists{top:878px;height:156px;color:#fff}
.lists h2{font-family:"Ubuntu",sans-serif;font-weight:700;font-size:14px;margin:13px 0 9px 15px}
.lists ul{list-style:none;margin-left:15px}
.lists li{font-size:8.6px;line-height:16px;padding-left:11px;position:relative}
.lists li::before{content:"";position:absolute;left:0;top:5px;border:3px solid transparent;border-left:3px solid #fff}
.latest{left:82px;width:222px;background:var(--orange)}
.latest li{color:#ffe8d2}
.popular{left:304px;width:223px;background:var(--plum)}
.fb{left:550px;top:507px;width:228px;height:334px;background:var(--fb)}
.fb .bar{position:absolute;left:10px;top:8px;width:208px;height:16px;background:#5b79b8;color:#fff;font-size:8.4px;font-weight:700;line-height:16px;padding-left:4px}
.fb .post{position:absolute;left:11px;width:206px;height:40px;border-bottom:1px dotted #6d87bd}
.fb .av{position:absolute;left:0;top:2px;width:32px;height:30px;background:linear-gradient(#ddd,#999)}
.fb .post b{position:absolute;left:38px;top:2px;font-size:8.5px;color:#fff}
.fb .post span{position:absolute;left:38px;top:14px;width:166px;font-size:7.2px;line-height:10px;color:#dfe6f4}
.fb .likes{position:absolute;left:14px;top:218px;width:204px;height:106px;background:#fff}
.fb .likes .t{font-size:6.3px;color:#333;padding:4px}
.fb .faces{display:grid;grid-template-columns:repeat(6,30px);gap:2px;margin-left:4px}
.fb .faces i{display:block;height:30px;background:linear-gradient(#cfc3b5,#8a7a6a)}
.fb .note{font-size:5.5px;color:#3b5998;padding:6px 4px}
.tw{left:550px;top:853px;width:228px;height:183px;background:var(--sky)}
.tw .name{position:absolute;left:10px;top:7px;font-family:"Ubuntu",sans-serif;font-size:8px;line-height:8px;color:#fff}
.tw .list{position:absolute;left:3px;top:33px;width:222px;height:124px;background:#fff;border-radius:3px}
.tw .tweet{position:relative;height:39px;border-bottom:1px solid #e4e4e4;padding:5px 0 0 34px;font-size:8.2px;line-height:10px;color:#222}
.tw .tweet i{position:absolute;left:5px;top:5px;width:22px;height:22px;background:linear-gradient(#c9b9a6,#7d6b58)}
.tw .tweet em{font-style:normal;color:#6aa82a}
.tw .tweet small{display:block;font-size:5.8px;color:#6aa82a}
.tw .join{position:absolute;left:0;bottom:3px;width:228px;text-align:center;font-size:8.5px;color:#fff}
.tw .bird{position:absolute;left:9px;bottom:4px;width:10px;height:10px;border-radius:50%;background:#fff}
.flogo{left:80px;top:1093px;font-family:"Ubuntu",sans-serif;font-weight:500;font-size:22px;line-height:20px;color:#fff}
.flogo .dot{display:inline-block;width:26px;height:26px;border:3px solid #fff;border-radius:50%;vertical-align:middle;margin-right:10px}
.fmeta{left:85px;top:1164px;font-size:8.6px;line-height:13px;color:#fff}
.fcol{top:1068px;color:#fff}
.fcol h4{font-size:10px;font-weight:700;margin-bottom:5px}
.fcol a{display:block;font-size:8.6px;line-height:17.3px;color:#fff;text-decoration:none}
.vdiv{top:1070px;width:0;height:118px;border-left:1px dotted #d8e9fa}
</style>
</head>
<body>
<div class="abs header"></div>
<div class="abs brand"><span class="dot"></span><span style="display:inline-block;vertical-align:middle">Furrow Cover<br>Polls UK</span></div>
<div class="abs social"><span>FaceFeed</span><span>ClipStream</span><span>Chirper</span><span>RSS</span></div>
<nav class="abs nav">
  <a class="active" href="#">Home</a><a href="#">Policies</a><a href="#">Glossary</a><a href="#">Fact Sheets</a><a href="#">Survey Reports</a><a href="#">News &amp; Comment</a>
</nav>
<div class="abs page"></div>

<section class="abs hero">
  <h1>An Independent website...</h1>
  <div class="l2">dedicated to helping you ...</div>
  <div class="l3">find the best insurance policy...</div>
  <div class="l4">for your pet</div>
  <div class="pets" role="img" aria-label="Group of dogs, cats, a parrot and a goldfish bowl"></div>
  <div class="btn-learn">Learn more</div>
</section>

<section class="abs policy">
  <h2>Check out a Policy</h2>
  <div class="field" style="top:37px"></div>
  <div class="field" style="top:74px"></div>
  <div class="go">Check Now</div>
</section>

<div class="abs ad" role="img" aria-label="Advert for Brightbowl Fresh Kitchen 14 day fresh food plan, www.brightbowlkitchen.com"></div>

<div class="abs welcome-icon"></div>
<section class="welcome"><h2>Welcome To Furrow Cover Polls Uk</h2></section>
<div class="abs welcome-pic" role="img" aria-label="Dogs, cats and a parrot sitting together"></div>
<div class="abs welcome-txt">
  <p>This is an independent website dedicated to helping you to find the best pet insurance policy for your pet</p>
  <p>Here you will find unbiased detailed information about almost all of the 205 pet insurance policies currently available in the UK (we hope the other 3 will follow shortly!)</p>
  <p>We do NOT sell any pet insurance policies nor do we receive commission from any insurance companies</p>
</div>
<div class="abs more">More Info</div>
<div class="abs rule" style="left:84px;top:598px;width:446px"></div>

<h2 class="abs news-h">News and Comments</h2>
<article class="abs news-item" style="top:640px">
  <h3>Pet Insurance - an introduction</h3>
  <p>We do NOT sell any pet insurance policies nor do we receive commission from any insurance companiesa-ny pet insurance policies nor do we receive commission from any insurance companies</p>
  <div class="rm">Readmore</div><div class="rule"></div>
</article>
<article class="abs news-item" style="top:702px">
  <h3>Pet Insurance - an introduction</h3>
  <p>We do NOT sell any pet insurance policies nor do we receive commission from any insurance companiesa-ny pet insurance policies nor do we receive commission from any insurance companies</p>
  <div class="rm">Readmore</div><div class="rule"></div>
</article>
<article class="abs news-item" style="top:763px">
  <h3>Pet Insurance - an introduction</h3>
  <p>We do NOT sell any pet insurance policies nor do we receive commission from any insurance companiesa-ny pet insurance policies nor do we receive commission from any insurance companies</p>
  <div class="rm">Readmore</div><div class="rule"></div>
</article>
<article class="abs news-item" style="top:824px">
  <h3>Pet Insurance - an introduction</h3>
  <p>We do NOT sell any pet insurance policies nor do we receive commission from any insurance</p>
  <div class="rm" style="margin-top:6px">Readmore</div><div class="rule"></div>
</article>

<section class="abs lists latest">
  <h2>Latest Reviews</h2>
  <ul><li>Pet Insurance - an introduction</li><li>Pet Insurance Policies - Know Your Terms</li><li>Vet Fees - Policy Types</li><li>Using Price Comparison Engines</li><li>Common Policy Terms</li><li>Pet Insurance Policies - Know Your Terms</li></ul>
</section>
<section class="abs lists popular">
  <h2>Popular Reviews</h2>
  <ul><li>Coming soon...</li><li>About Furrow Cover Polls UK</li><li>An idea is born!</li><li>Coming soon...</li><li>About Furrow Cover Polls UK</li><li>An idea is born!</li></ul>
</section>

<section class="abs fb">
  <div class="bar">Find us on FaceFeed</div>
  <div class="post" style="top:34px"><div class="av"></div><b>Dana Wren</b><span>We do NOT sell any pet insurance policies nor do we receive commission...</span></div>
  <div class="post" style="top:80px"><div class="av"></div><b>Dana Wren</b><span>We do NOT sell any pet insurance policies nor do we receive commission...</span></div>
  <div class="post" style="top:126px"><div class="av"></div><b>Dana Wren</b><span>We do NOT sell any pet insurance policies nor do we receive commission...</span></div>
  <div class="post" style="top:172px;border:0"><div class="av"></div><b>Dana Wren</b><span>We do NOT sell any pet insurance policies nor do we receive commission...</span></div>
  <div class="likes">
    <div class="t">You and 14,596 others like <span style="color:#3b5998">Dana Wren</span>.</div>
    <div class="faces"><i></i><i></i><i></i><i></i><i></i><i></i><i></i><i></i><i></i><i></i></div>
    <div class="note">FaceFeed social plugin</div>
  </div>
</section>

<section class="abs tw">
  <div class="name">Furrow Cover<br>Polls UK</div>
  <div class="list">
    <div class="tweet"><i></i><em>plainblogpointers</em> Cool Floating Recent Tweets Widget for Blogs<small>11 minutes ago · reply · retweet · favorite</small></div>
    <div class="tweet"><i></i><em>plainblogpointers</em> Giveaway: 5 Web Hosting Accounts From Hostvale<small>4 hours ago · reply · retweet · favorite</small></div>
    <div class="tweet" style="border:0"><i></i><em>coinharbor</em> 5 Question to Ask Before Using AdLedger<small>4 days ago · reply · retweet · favorite</small></div>
  </div>
  <div class="bird"></div>
  <div class="join">Join the conversation</div>
</section>

<div class="abs flogo"><span class="dot"></span><span style="display:inline-block;vertical-align:middle">Furrow Cover<br>Polls UK</span></div>
<div class="abs fmeta">Privacy PolicyLegal About Furrow Cover Polls UK<br>copyright © Furrow Cover Policy Polls</div>
<div class="abs vdiv" style="left:397px"></div>
<div class="abs vdiv" style="left:634px"></div>
<div class="abs fcol" style="left:435px"><h4>Site Map</h4><a>Find a Vet</a><a>Learn</a><a>Care</a><a>Train</a><a>Shop</a><a>Sitemap</a></div>
<div class="abs fcol" style="left:540px"><h4>Links</h4><a>About Us</a><a>Privacy Policy</a><a>Terms of Use</a><a>Contact Us</a><a>Media Kit</a></div>
<div class="abs fcol" style="left:670px"><h4>Follow Us</h4><a>FaceFeed</a><a>Chirper</a><a>Orbit+</a><a>Pinboardly</a><a>ClipStream</a></div>
</body>
</html>
```